Brightacre - online store for farm produce

Online store selling fresh produce (vegetables, fruits, dairy products, meat, ...) from various farmers. Every farm has its own shopping window - order page - just like a really simple web store.

Please check the attached design brief and mock-ups for further details.

Target Market(s)

People looking for fresh vegetables, fruit, meat, ... delivered from farms

Industry/Entity Type

Farming

Coding

Coded - Design and coding required

Number of Pages Required

5+ page

Font styles to use
Sans Serif

Requirements
Must have
• Custom design. Good UX/UI design, very functional.
Responsive using bootstrap 12 point grid system

```html
<!DOCTYPE html>
<html lang="en">
<head>
<meta charset="utf-8">
<title>Brightacre – Fresh produce from farms</title>
<link href="https://fonts.googleapis.com/css2?family=Poppins:wght@400;500;600;700&display=swap" rel="stylesheet">
<style>
:root{
  --green-light:#66b02c;
  --green:#4c9a2a;
  --green-dark:#2f7a2f;
  --button:#1f8a3b;
  --ink:#222;
  --text:#3a3a3a;
  --footer:#242424;
  --white:#fff;
}
*{box-sizing:border-box;margin:0;padding:0}
html,body{width:1200px;height:3489px;overflow:hidden}
body{position:relative;font-family:"Poppins",sans-serif;color:var(--text);background:var(--white)}
.abs{position:absolute}

/* header */
.site-header{position:absolute;left:0;top:0;width:1200px;height:133px;background:var(--white)}
.brand{position:absolute;left:111px;top:38px;font-size:38px;font-weight:700;color:var(--green);letter-spacing:.5px}
.social-tab{position:absolute;left:853px;top:0;width:230px;height:51px;background:var(--green);border-radius:0 0 30px 30px;display:flex;gap:14px;justify-content:center;align-items:center}
.social-tab span{width:14px;height:14px;border-radius:50%;background:var(--white)}
.main-nav{position:absolute;top:84px;left:512px;display:flex;gap:26px;font-size:18px;color:var(--ink)}
.main-nav a{color:inherit;text-decoration:none}
.main-nav .active{color:var(--green);font-weight:600}

/* hero */
.hero-photo{position:absolute;left:0;top:133px;width:1200px;height:700px;background:linear-gradient(120deg,#7d6f63 0%,#b49d88 25%,#6f7d4e 55%,#3d3b34 80%,#5e3a32 100%)}
.hero-wave{position:absolute;left:0;top:133px}
.hero-circle{position:absolute;left:634px;top:165px;width:446px;height:446px;border-radius:50%;background:rgba(20,45,20,.82)}
.hero-title{position:absolute;left:634px;top:240px;width:446px;text-align:center;color:var(--white);font-size:60px;font-weight:700}
.hero-text{position:absolute;left:634px;top:384px;width:446px;text-align:center;color:var(--white);font-size:19px;line-height:27.5px}
.btn{position:absolute;display:flex;align-items:center;justify-content:center;background:var(--button);color:var(--white);border-radius:30px;font-weight:600;font-size:15px;text-transform:uppercase}
.hero-btn{left:792px;top:492px;width:129px;height:54px;background:var(--green);text-transform:none;font-weight:500;font-size:18px}

/* sections */
.photo{position:absolute;width:600px;height:428px}
.photo-left{left:0;border-radius:0 230px 200px 0}
.photo-right{left:600px;border-radius:230px 0 0 200px}
.section-title{position:absolute;font-size:36px;font-weight:600;color:var(--green-dark);white-space:nowrap}
.section-title em{font-style:normal;color:var(--green-light)}
.copy{position:absolute;width:440px;font-size:14px;line-height:22.5px;text-align:justify}
.ticks{position:absolute;list-style:none;font-size:14px;line-height:25px}
.ticks li{position:relative;padding-left:28px}
.ticks li::before{content:"";position:absolute;left:0;top:8px;width:14px;height:9px;background:var(--green);border-radius:0 10px 0 10px;transform:rotate(-30deg)}
.field{position:absolute;width:187px;height:51px;border:1.5px solid #888;border-radius:30px;font-size:16px;padding-left:16px;display:flex;align-items:center;color:var(--ink)}

/* footer */
.footer-bg{position:absolute;left:0;top:2860px}
.footer-head{position:absolute;top:3136px;color:var(--white);font-size:24px;font-weight:600}
.footer-links{position:absolute;left:111px;top:3185px;list-style:none;color:var(--white);font-size:16px;line-height:25.7px}
.contact{position:absolute;left:349px;display:flex;align-items:center;gap:14px;color:var(--white);font-size:15px;line-height:22px}
.contact .ico{flex:none;width:40px;height:40px;border:1.5px solid var(--white);border-radius:50%;display:flex;align-items:center;justify-content:center}
.footer-brand{position:absolute;left:850px;top:3175px;width:230px;text-align:center;font-size:38px;font-weight:700;color:var(--green-light)}
.circle-link{position:absolute;top:3296px;width:62px;height:62px;border:1.5px solid var(--white);border-radius:50%}
.rule{position:absolute;left:112px;top:3404px;width:975px;height:1px;background:#bbb}
.copyright{position:absolute;left:0;top:3438px;width:1200px;text-align:center;color:var(--white);font-size:15px;font-weight:500}
</style>
</head>
<body>

<header class="site-header">
  <div class="brand">Brightacre</div>
  <div class="social-tab"><span></span><span></span><span></span><span></span><span></span></div>
  <nav class="main-nav">
    <a class="active" href="#">Home</a>
    <a href="#">Current Offer</a>
    <a href="#">Farm Directory</a>
    <a href="#">Settings</a>
    <a href="#">Farmer Login</a>
  </nav>
</header>

<section class="hero">
  <div class="hero-photo" role="img" aria-label="Photo of a smiling woman buying fresh vegetables at a market stall"></div>
  <svg class="hero-wave" width="1200" height="700" viewBox="0 133 1200 700" aria-hidden="true">
    <path d="M0,735 C250,840 460,800 700,725 S1050,640 1200,700 L1200,833 L0,833 Z" fill="var(--green)"/>
    <path d="M0,758 C240,850 470,820 710,745 S1060,665 1200,720 L1200,833 L0,833 Z" fill="var(--white)"/>
  </svg>
  <div class="hero-circle"></div>
  <h1 class="hero-title">Brightacre</h1>
  <p class="hero-text">We are an online store selling fresh produce (vegetables, fruits, dairy products, meat, ...) from various farmers</p>
  <a class="btn hero-btn">Read More</a>
</section>

<section class="about">
  <div class="photo photo-left" style="top:940px;background:linear-gradient(135deg,#5f7d3a,#9bb05a 40%,#b94a3c 75%,#6b5a3a)" role="img" aria-label="Photo of a basket full of radishes, peppers, lettuce and cucumbers"></div>
  <h2 class="section-title" style="left:646px;top:1008px"><em>What</em> Is This About</h2>
  <p class="copy" style="left:646px;top:1072px">Nemo enim ipsam voluptatem quia voluptas sit aspernatur aut odit aut fugit, sed quia con sequuntur magni dolores eos qui ra tione voluptatem.</p>
  <p class="copy" style="left:646px;top:1151px">Neque porro quisquam est, qui dolorem ipsum quia dolor sit amet, consectetur, adipisci velit, sed quia non numquam eius modi tempora incidunt.</p>
  <a class="btn" style="left:646px;top:1238px;width:161px;height:51px">Product Search</a>
</section>

<section class="farmers">
  <h2 class="section-title" style="left:111px;top:1457px"><em>Benefits</em> For Farmer</h2>
  <ul class="ticks" style="left:111px;top:1520px">
    <li>Nemo enim ipsam voluptatem.</li>
    <li>Quia voluptas sit aspernatur aut odit.</li>
    <li>Aut fugit, sed quia con sequuntur magni.</li>
    <li>Dolores eos qui ra tione voluptatem.</li>
    <li>Nemo enim ipsam voluptatem.</li>
    <li>Quia voluptas sit aspernatur aut odit.</li>
  </ul>
  <div class="field" style="left:111px;top:1694px">Name</div>
  <div class="field" style="left:309px;top:1694px">Phone</div>
  <div class="field" style="left:111px;top:1757px">Email</div>
  <a class="btn" style="left:309px;top:1757px;width:127px;height:51px">Submit Now</a>
  <div class="photo photo-right" style="top:1396px;background:radial-gradient(circle at 55% 60%,#f2b35a,#b8652a 35%,#3a2418 80%)" role="img" aria-label="Silhouette of two farmers shaking hands in a field at sunset"></div>
</section>

<section class="customers">
  <div class="photo photo-left" style="top:1886px;background:linear-gradient(120deg,#8c7a64,#c9b49a 40%,#8aa65a 70%,#6d8a4a)" role="img" aria-label="Photo of two women choosing vegetables at a market"></div>
  <h2 class="section-title" style="left:645px;top:1946px"><em>Benefits</em> For Customers</h2>
  <ul class="ticks" style="left:645px;top:2010px">
    <li>Nemo enim ipsam voluptatem.</li>
    <li>Quia voluptas sit aspernatur aut odit.</li>
    <li>Aut fugit, sed quia con sequuntur magni.</li>
    <li>Dolores eos qui ra tione voluptatem.</li>
    <li>Nemo enim ipsam voluptatem.</li>
  </ul>
  <p class="copy" style="left:646px;top:2150px">Neque porro quisquam est, qui dolorem ipsum quia dolor sit amet, consectetur, adipisci velit.</p>
  <a class="btn" style="left:646px;top:2218px;width:161px;height:51px">Product Search</a>
</section>

<section class="featured">
  <h2 class="section-title" style="left:111px;top:2407px"><em>Featured</em> Farm Or Product</h2>
  <p class="copy" style="left:111px;top:2478px">Nemo enim ipsam voluptatem quia voluptas sit aspernatur aut odit aut fugit, sed quia con sequuntur magni dolores eos qui ra tione voluptatem.</p>
  <p class="copy" style="left:111px;top:2556px">Neque porro quisquam est, qui dolorem ipsum quia dolor sit amet, consectetur, adipisci velit, sed quia non numquam eius modi tempora incidunt.</p>
  <a class="btn" style="left:111px;top:2645px;width:110px;height:51px">Farm</a>
  <div class="photo photo-right" style="top:2348px;background:linear-gradient(135deg,#3f5a34,#8fae6a 45%,#c9d8b0 70%,#a5472e)" role="img" aria-label="Photo of hands tending tomato plants in a greenhouse"></div>
</section>

<footer class="site-footer">
  <svg class="footer-bg" width="1200" height="629" viewBox="0 2860 1200 629" aria-hidden="true">
    <path d="M0,2990 C200,3040 420,3020 640,2960 S1000,2850 1200,2960 L1200,3489 L0,3489 Z" fill="var(--green)"/>
    <path d="M0,3010 C210,3070 430,3050 650,2985 S1010,2880 1200,2990 L1200,3489 L0,3489 Z" fill="var(--white)"/>
    <path d="M0,3030 C220,3095 440,3075 660,3005 S1020,2905 1200,3000 L1200,3489 L0,3489 Z" fill="var(--footer)"/>
  </svg>
  <h3 class="footer-head" style="left:111px">QUICK LINKS</h3>
  <ul class="footer-links">
    <li>Home</li><li>Shop</li><li>Current Offer</li><li>About Us</li><li>Contact</li><li>Testimonial</li>
  </ul>
  <h3 class="footer-head" style="left:350px">QUICK LINKS</h3>
  <div class="contact" style="top:3191px">
    <span class="ico"><svg width="18" height="22" viewBox="0 0 18 22"><path d="M9 21s-7-7.5-7-12a7 7 0 0 1 14 0c0 4.5-7 12-7 12z" fill="none" stroke="#fff" stroke-width="1.6"/><circle cx="9" cy="9" r="2.6" fill="none" stroke="#fff" stroke-width="1.6"/></svg></span>
    <span>48 Orchard Lane, Millbrook Valley,<br>MV 204 718</span>
  </div>
  <div class="contact" style="top:3252px">
    <span class="ico"><svg width="20" height="20" viewBox="0 0 20 20"><path d="M4 2l3 0 1.5 4-2 1.5a11 11 0 0 0 6 6L14 11.5l4 1.5v3a2 2 0 0 1-2 2A15 15 0 0 1 2 4a2 2 0 0 1 2-2z" fill="none" stroke="#fff" stroke-width="1.5"/></svg></span>
    <span>+100 555 0142</span>
  </div>
  <div class="contact" style="top:3303px">
    <span class="ico"><svg width="20" height="16" viewBox="0 0 20 16"><rect x="1" y="1" width="18" height="14" fill="none" stroke="#fff" stroke-width="1.5"/><path d="M1 1l9 8 9-8" fill="none" stroke="#fff" stroke-width="1.5"/></svg></span>
    <span>hello@brightacre-market.com</span>
  </div>
  <div class="footer-brand">Brightacre</div>
  <span class="circle-link" style="left:854px"></span>
  <span class="circle-link" style="left:933px"></span>
  <span class="circle-link" style="left:1010px"></span>
  <div class="rule"></div>
  <p class="copyright">Copyrights @ 2020 Brightacre. All Rights Reserved.</p>
</footer>

</body>
</html>
```